Lumokrest Mobile App

I need a professional, sleek design for a new mobile application for Zentab. The application will be the mobile counterpart to the current website (www.lumokrest-app.net - please refer to site for existing web design).
Lumokrest is a photo social network which focuses on content aggregation, search and real-time photo discovery.
I need a clean, modern, minimalistic design for the mobile app which will run on Zentab, including minimalistic page and button designs.
I've attached undesigned screenshots of the current application build to give an idea of the functionality and pages available within the application.
The app will have the following pages/functionality:
- photo feed of other users' images; data presented: photo, photo caption, user name, date
- upload photo
- save photo
- photo search; available search criteria: keywords, dates (from/to), location
Photographers/Photo enthusiasts, bloggers, social networking
Build

```html
<!DOCTYPE html>
<html lang="en">
<head>
<meta charset="utf-8">
<title>Lumokrest – Upload</title>
<link href="https://fonts.googleapis.com/css2?family=Open+Sans:wght@400;600;700&display=swap" rel="stylesheet">
<style>
  :root{
    --bg-top:#343a42;
    --bg-bottom:#23272d;
    --brand-blue:#1e9ee0;
    --text-light:#f2f4f6;
    --text-muted:#c9ced4;
    --tile-top:#4a515b;
    --tile-bottom:#363c45;
    --tile-border:#23272d;
    --active-top:#6fdc5e;
    --active-bottom:#3fc23a;
    --signout-top:#8ec06a;
    --signout-bottom:#5f9a43;
    --icon-plum:#6b3a5c;
    --badge-blue:#3f72c4;
    --field-white:#ffffff;
    --field-text:#333a40;
    --divider:#15181c;
    --divider-light:#454b53;
    --search-bg:#1f2328;
    --search-green:#3eb83a;
  }
  *{box-sizing:border-box;margin:0;padding:0}
  html,body{width:960px;height:1200px;overflow:hidden}
  body{
    font-family:"Open Sans",Arial,sans-serif;
    background:linear-gradient(180deg,var(--bg-top),var(--bg-bottom));
    position:relative;color:var(--text-light);
  }
  .brand{position:absolute;left:40px;top:34px;display:flex;align-items:center;gap:14px}
  .brand-mark{width:26px;height:26px;background:var(--brand-blue);border-radius:4px}
  .brand-name{font-size:48px;font-weight:400;color:var(--brand-blue);letter-spacing:3px;line-height:1}
  .tagline{position:absolute;left:188px;top:100px;font-size:17px;font-weight:700;color:var(--text-light)}
  .search{
    position:absolute;left:548px;top:45px;width:224px;height:54px;border-radius:8px;
    background:var(--search-bg);box-shadow:inset 0 2px 4px rgba(0,0,0,.5);
    display:flex;align-items:center;justify-content:space-between;padding:0 14px 0 18px;
    font-size:17px;color:#9aa1a9
  }
  .search-btn{width:28px;height:28px;border-radius:6px;background:var(--search-green);display:flex;align-items:center;justify-content:center}
  .signout{
    position:absolute;left:784px;top:46px;width:138px;height:53px;border-radius:4px;
    background:linear-gradient(var(--signout-top),var(--signout-bottom));
    font-size:17px;font-weight:700;color:#fff;display:flex;align-items:center;justify-content:center
  }
  .divider{position:absolute;left:18px;top:142px;width:924px;height:2px;border-top:1px solid var(--divider);border-bottom:1px solid var(--divider-light)}
  .nav-tile{
    position:absolute;top:192px;width:163px;height:135px;border-radius:10px;
    background:linear-gradient(var(--tile-top),var(--tile-bottom));
    border:1px solid var(--tile-border);box-shadow:0 3px 6px rgba(0,0,0,.4);
    display:flex;flex-direction:column;align-items:center;justify-content:center;gap:14px;
    font-size:23px;color:var(--text-light)
  }
  .nav-tile.active{background:linear-gradient(var(--active-top),var(--active-bottom));color:#2a3a2a}
  .nav-home{left:210px}.nav-upload{left:398px}.nav-profile{left:586px}
  .photo{
    position:absolute;left:33px;top:372px;width:893px;height:411px;border-radius:9px;
    background:linear-gradient(180deg,#8f969c 0%,#7a8377 22%,#5f6f48 45%,#4c5d36 70%,#3c4a2c 100%);
    border:1px solid #5a6068
  }
  .upload-badge{
    position:absolute;left:309px;top:534px;width:386px;height:87px;border-radius:6px;
    background:var(--badge-blue);display:flex;align-items:center;justify-content:center;gap:18px;
    font-size:22px;color:#fff;box-shadow:0 2px 6px rgba(0,0,0,.3)
  }
  .caption-field{
    position:absolute;left:33px;top:807px;width:893px;height:93px;border-radius:12px;
    background:var(--field-white);box-shadow:inset 0 0 8px rgba(0,0,0,.35);
    font-size:22px;color:var(--field-text);padding-left:31px;display:flex;align-items:center
  }
  .action-btn{
    position:absolute;height:66px;border-radius:6px;
    background:linear-gradient(#535a64,#3b4149);border:1px solid #262a30;
    box-shadow:0 2px 4px rgba(0,0,0,.45);
    display:flex;align-items:center;justify-content:center;gap:16px;
    font-size:22px;color:var(--text-light)
  }
  .btn-upload{left:95px;top:920px;width:210px;background:linear-gradient(#7c848e,#5d646d)}
  .btn-save{left:322px;top:920px;width:313px}
  .btn-cancel{left:652px;top:920px;width:209px}
  .btn-share{left:375px;top:1083px;width:209px}
</style>
</head>
<body>
  <header>
    <div class="brand"><span class="brand-mark"></span><span class="brand-name">Lumokrest</span></div>
    <p class="tagline">what did you see today ...</p>
    <div class="search">Search
      <span class="search-btn"><svg width="16" height="16" viewBox="0 0 16 16"><circle cx="6.5" cy="6.5" r="4.5" fill="none" stroke="#fff" stroke-width="2"/><line x1="10" y1="10" x2="14" y2="14" stroke="#fff" stroke-width="2.5"/></svg></span>
    </div>
    <div class="signout">SIGNOUT</div>
    <div class="divider"></div>
  </header>

  <nav>
    <div class="nav-tile nav-home">
      <svg width="44" height="40" viewBox="0 0 44 40"><path d="M22 3 3 20h6v17h10V26h6v11h10V20h6z" fill="var(--icon-plum)"/></svg>HOME
    </div>
    <div class="nav-tile nav-upload active">
      <svg width="46" height="36" viewBox="0 0 46 36"><path d="M4 18h10l4 6h10l4-6h10v14H4z" fill="#3b3f45"/><path d="M23 3 13 14h6v8h8v-8h6z" fill="#fff"/></svg>UPLOAD
    </div>
    <div class="nav-tile nav-profile">
      <svg width="44" height="44" viewBox="0 0 44 44"><circle cx="22" cy="13" r="10" fill="var(--icon-plum)"/><path d="M3 44c0-12 8-19 19-19s19 7 19 19z" fill="var(--icon-plum)"/></svg>PROFILE
    </div>
  </nav>

  <main>
    <div class="photo" role="img" aria-label="Uploaded landscape photo of green fields, hedgerows and houses under misty sky"></div>
    <div class="upload-badge">
      <svg width="40" height="34" viewBox="0 0 40 34"><path d="M3 18l11 11L37 4" fill="none" stroke="#fff" stroke-width="7" stroke-linecap="round" stroke-linejoin="round"/></svg>SUCESSFULLY UPLOADED
    </div>
    <div class="caption-field">marcus.oduya taken</div>

    <div class="action-btn btn-upload">
      <svg width="40" height="30" viewBox="0 0 46 36"><path d="M4 18h10l4 6h10l4-6h10v14H4z" fill="var(--icon-plum)"/><path d="M23 3 13 14h6v8h8v-8h6z" fill="#fff"/></svg>UPLOAD
    </div>
    <div class="action-btn btn-save">
      <svg width="48" height="38" viewBox="0 0 48 38"><rect x="2" y="2" width="44" height="34" rx="3" fill="var(--icon-plum)"/><rect x="7" y="7" width="34" height="24" fill="#4f5560"/><path d="M7 31l11-12 8 8 6-5 9 9z" fill="#8a5b7d"/><circle cx="33" cy="13" r="3" fill="#8a5b7d"/></svg>SAVE TO PHOTO
    </div>
    <div class="action-btn btn-cancel">
      <svg width="44" height="44" viewBox="0 0 44 44"><circle cx="22" cy="22" r="20" fill="#5a616b" stroke="#2a2e34" stroke-width="2"/><path d="M14 14l16 16M30 14 14 30" stroke="var(--icon-plum)" stroke-width="5" stroke-linecap="round"/></svg>CANCEL
    </div>
    <div class="action-btn btn-share">
      <svg width="40" height="30" viewBox="0 0 40 30"><path d="M2 7h8c8 0 12 16 20 16h3M2 23h8c8 0 12-16 20-16h3" fill="none" stroke="var(--icon-plum)" stroke-width="4"/><path d="M32 1l7 6-7 6zM32 17l7 6-7 6z" fill="var(--icon-plum)"/></svg>SHARE
    </div>
  </main>
</body>
</html>
```